TOVR Business Card Colin

Tor Valley Resources (TOVR) is a consulting company that advises stakeholders in the Agricultural Industry. Based in rural NSW Australia, we need a good business card. TOVR has a lifetime of agricultural experience and knowledge, particularly in the beef, wool and lamb markets. Though it is expanding into other rural ventures. Our clients are primarily off-farm investors who trust our business to advise on the best path forward for their agricultural investment. We also work with large players in the retail sector. Our image is trustworthy, reliable, smart and professional.
Updates

I think the black is too urban, perhaps a dark blue on one side and white on the other, or the yellow/orange on one side and white on the other??

we need to have the tag line "Customised Agribusiness Strategy" and our list of services:

"Due Diligence, Acquisition, Planning, Management, Strategy, Supply Chain" included in the design

we actually have 6 services - the should read in order:

Due diligence
Acquisition
Strategy
Planning 
Management
Supply chain

Target Market(s)

large rural land holders
senior players in agribusiness
senior management of retail food outlets
middle-senior aged men

Industry/Entity Type

Retail

Requirements
Must have
• high quality, 2 sides

logo

"Colin Hartley
Director
0491735260
colin@tovr-example.com.au
PO Box 4726, Tarrowee NSW 2399"

tag line "Customised Agribusiness Strategy"

services provided

"Due diligence
Acquisition
Strategy
Planning
Management
Supply chain"
Should not have
• no images of animals or leaves

```html
<!DOCTYPE html>
<html lang="en">
<head>
<meta charset="utf-8">
<title>TOVR Business Card – Colin Hartley</title>
<link rel="stylesheet" href="https://fonts.googleapis.com/css2?family=Open+Sans:ital,wght@0,400;0,600;1,400&display=swap">
<style>
  :root {
    --backdrop: #ecebe8;
    --card: #ffffff;
    --navy: #2b4a8b;
    --blue: #4a6fb5;
    --gold: #f2b632;
    --orange: #e59a1c;
    --ink: #4a4a4a;
    --muted: #707070;
    --icon: #8a8a8a;
  }
  html, body {
    margin: 0;
    width: 1200px;
    height: 871px;
    overflow: hidden;
    background: var(--backdrop);
    font-family: "Open Sans", Arial, sans-serif;
  }
  .sheet {
    position: relative;
    width: 1200px;
    height: 871px;
  }
  .card {
    position: absolute;
    top: 150px;
    width: 340px;
    height: 570px;
    background: var(--card);
    box-shadow: 0 6px 22px rgba(0,0,0,0.18);
    overflow: hidden;
  }
  .card--front { left: 220px; }
  .card--back { left: 640px; }

  .brand {
    position: absolute;
    top: 60px;
    color: var(--navy);
    font-weight: 600;
  }
  .card--front .brand { left: 40px; }
  .card--back .brand { right: 36px; text-align: right; }
  .brand__row { display: flex; align-items: center; gap: 12px; }
  .card--back .brand__row { justify-content: flex-end; }
  .brand__dot {
    width: 18px; height: 18px; border-radius: 50%;
    background: var(--navy);
  }
  .brand__name { font-size: 54px; line-height: 1; letter-spacing: 1px; }
  .brand__full {
    margin-top: 6px;
    font-size: 13px;
    letter-spacing: 2px;
    text-transform: uppercase;
  }

  .stripes { position: absolute; height: 14px; }
  .stripes::before, .stripes::after {
    content: ""; position: absolute; left: 0; right: 0; height: 5px;
  }
  .stripes::before { top: 0; background: var(--navy); }
  .stripes::after { bottom: 0; background: var(--gold); }

  .person { position: absolute; top: 228px; left: 0; right: 0; }
  .person .stripes { left: 0; width: 38px; top: 8px; }
  .person__name {
    margin-left: 50px; font-size: 20px; color: var(--ink);
  }
  .person__role {
    margin-left: 60px; font-size: 15px; font-style: italic; color: var(--muted);
  }

  .contact {
    position: absolute; top: 368px; left: 84px;
    font-size: 16px; color: var(--muted); line-height: 24px;
  }
  .contact__line { display: flex; align-items: center; gap: 10px; }
  .contact__line svg { width: 18px; height: 18px; flex: none; }
  .contact__address { margin-bottom: 2px; }

  .card .stripes--foot { left: 0; right: 0; bottom: 62px; }

  .tagline {
    position: absolute; top: 218px; right: 40px;
    text-align: right; color: var(--navy); font-size: 15px; line-height: 19px;
  }
  .card--back .stripes--tag { right: 0; width: 32px; top: 240px; }
  .services {
    position: absolute; top: 284px; right: 40px; margin: 0; padding: 0;
    list-style: none; text-align: right; color: var(--orange);
    font-size: 16px; line-height: 26px;
  }
</style>
</head>
<body>
<main class="sheet">

  <section class="card card--front" aria-label="Business card front">
    <div class="brand">
      <div class="brand__row">
        <span class="brand__name">TOVR</span>
        <span class="brand__dot"></span>
      </div>
      <div class="brand__full">Tor Valley Resources</div>
    </div>

    <div class="person">
      <span class="stripes"></span>
      <div class="person__name">Colin Hartley</div>
      <div class="person__role">Director</div>
    </div>

    <div class="contact">
      <div class="contact__address">PO Box 4726,<br>Tarrowee NSW 2399</div>
      <div class="contact__line">
        <svg viewBox="0 0 24 24" aria-hidden="true"><path fill="var(--icon)" d="M6.6 10.8a15.1 15.1 0 0 0 6.6 6.6l2.2-2.2c.3-.3.7-.4 1-.2 1.1.4 2.3.6 3.6.6.6 0 1 .4 1 1V20c0 .6-.4 1-1 1A17 17 0 0 1 3 4c0-.6.4-1 1-1h3.5c.6 0 1 .4 1 1 0 1.3.2 2.5.6 3.6.1.3 0 .7-.2 1z"/></svg>
        <span>(04) 9173-5260</span>
      </div>
      <div class="contact__line">
        <svg viewBox="0 0 24 24" aria-hidden="true"><rect x="2.5" y="5.5" width="19" height="13" fill="none" stroke="var(--icon)" stroke-width="1.5"/><path d="M2.5 5.5 12 13l9.5-7.5" fill="none" stroke="var(--icon)" stroke-width="1.5"/></svg>
        <span>colin@tovr-example.com.au</span>
      </div>
    </div>

    <span class="stripes stripes--foot"></span>
  </section>

  <section class="card card--back" aria-label="Business card back">
    <div class="brand">
      <div class="brand__row">
        <span class="brand__name">TOVR</span>
        <span class="brand__dot"></span>
      </div>
      <div class="brand__full">Tor Valley Resources</div>
    </div>

    <div class="tagline">Customised Agribusiness<br>Strategy</div>
    <span class="stripes stripes--tag"></span>

    <ul class="services">
      <li>Due diligence</li>
      <li>Acquisition</li>
      <li>Strategy</li>
      <li>Planning</li>
      <li>Management</li>
      <li>Supply chain</li>
    </ul>

    <span class="stripes stripes--foot"></span>
  </section>

</main>
</body>
</html>
```